Professional educational and informative brochures for CPAP alternative treatment for sleep apnea

I am a dentist who practices dental sleep medicine, alternative to CPAP, such as custom-fit oral appliance therapy, laser treatment, and other adjunctive treatments. I need a professional trifold brochure to give directly to patients and physicians. The brochure needs to be educational and informative, and I would also like it to provide some information about me from a marketing standpoint. I had a custom brochure made in the past, more catered for patients, but it looks too crowded with info and hard to read. I need a clean and easy-to-read brochure. It could be tri-fold or quarter-fold. I attached some files on my current brochure, business card, and logos for your review and ideas.
Updates

Nothing really caught my attention. Plus most of them are out of target of what I am looking for. I put more specific info on my project.

Target Market(s)

Referring physicians and self referred patients who seeks CPAP alternative treatments

Industry/Entity Type

Healthcare

Requirements
Must have
• a message that emphasizes that I can provide treatments alternative to CPAP for sleep apnea patients who do not tolerate CPAP
Nice to have
• pictures of each treatments I provide instead of CPAP
Should not have
• a message that confuses people that I am promoting CPAP as a CPAP provider because I am not!

```html
<!DOCTYPE html>
<html lang="en">
<head>
<meta charset="utf-8">
<title>Starlit Sleep Dentistry – Trifold Brochure</title>
<link href="https://fonts.googleapis.com/css2?family=Quicksand:wght@400;500;600;700&display=swap" rel="stylesheet">
<style>
  :root{
    --teal:#33687a;
    --teal-dark:#2b5a6b;
    --rust:#b05e3c;
    --cream:#fdfaf2;
    --brown:#5b3e34;
    --peach:#e5b7a2;
    --page:#949494;
    --white:#ffffff;
  }
  *{margin:0;padding:0;box-sizing:border-box}
  html,body{width:766px;height:1200px;overflow:hidden;background:var(--page)}
  body{font-family:"Quicksand",sans-serif;position:relative}
  .sheet-art{position:absolute;left:27px;width:711px;height:549px;overflow:hidden}
  .sheet-outside{top:35px}
  .sheet-inside{top:615px}
  .block{position:absolute}
  .heading{font-weight:700;font-size:20.5px;line-height:24px;letter-spacing:.1px}
  .light{color:var(--cream)}
  .body-copy{font-size:8.5px;line-height:12.6px;font-weight:500}
  .tick-list{list-style:none}
  .tick-list li{position:relative;padding-left:13px;font-size:8.5px;line-height:12.4px;font-weight:500}
  .tick-list li svg{position:absolute;left:0;top:2.3px;width:8px;height:8px}
  .on-teal li svg{color:var(--white);stroke:var(--teal)}
  .on-rust li svg{color:var(--white);stroke:var(--rust)}
  .doctor-name{font-weight:700;font-size:13.5px;text-align:center;color:var(--white)}
  .doctor-bio{color:var(--white);text-align:center;font-size:8.3px;line-height:13.2px;font-weight:500}
  .doctor-bio p+p{margin-top:6px}
  .brand{color:var(--brown);text-align:center;font-weight:500}
  .cover-title{font-weight:600;font-size:34px;line-height:34px;text-align:center;color:var(--brown)}
  .cover-title .accent{color:var(--teal)}
  .contact{color:var(--white);text-align:center;font-weight:700}
  .contact svg{width:9px;height:9px;vertical-align:-1px;margin-right:4px}
  .consequence-title{color:var(--brown);font-weight:700;font-size:20px;line-height:24px;text-align:center}
  .conditions{color:var(--brown);font-size:8.3px;line-height:14.6px;font-weight:500}
  .conditions .group{margin-bottom:11px}
  .conditions .group.tight{margin-bottom:2px}
  .conditions .two-line{line-height:11.5px;margin:1.5px 0 2px}
</style>
</head>
<body>

<svg width="0" height="0" style="position:absolute">
  <symbol id="tick" viewBox="0 0 16 16">
    <circle cx="8" cy="8" r="8" fill="currentColor"/>
    <path d="M4.5 8.3l2.4 2.3 4.6-4.9" fill="none" stroke-width="2" stroke-linecap="round" stroke-linejoin="round"/>
  </symbol>
</svg>

<!-- ============ OUTSIDE SHEET ============ -->
<svg class="sheet-art sheet-outside" viewBox="55 70 1428 1102" preserveAspectRatio="none">
  <defs>
    <linearGradient id="sleeperTone" x1="0" y1="0" x2="1" y2="1">
      <stop offset="0" stop-color="#cfc9c4"/><stop offset=".5" stop-color="#eeece9"/><stop offset="1" stop-color="#d9d5d1"/>
    </linearGradient>
    <linearGradient id="wakerTone" x1="0" y1="0" x2="1" y2="1">
      <stop offset="0" stop-color="#cfcbc6"/><stop offset=".6" stop-color="#b9b2ab"/><stop offset="1" stop-color="#e1ddd8"/>
    </linearGradient>
    <linearGradient id="portraitTone" x1="0" y1="0" x2="0" y2="1">
      <stop offset="0" stop-color="#d8cfc6"/><stop offset="1" stop-color="#5c4a40"/>
    </linearGradient>
  </defs>
  <rect x="55" y="70" width="476" height="1102" fill="var(--teal)"/>
  <rect x="530" y="70" width="477" height="1102" fill="var(--rust)"/>
  <rect x="1007" y="70" width="476" height="1102" fill="var(--cream)"/>
  <path d="M1483 350 L1483 775 L1310 600 Q1280 570 1310 540 Z" fill="var(--peach)"/>
  <path d="M1483 555 L1372 668 Q1345 700 1372 730 L1483 842" fill="none" stroke="var(--teal)" stroke-width="3"/>
  <path role="img" aria-label="Photo of a woman sleeping peacefully under white bedding" d="M590 70 L1483 70 L1483 345 L1245 668 Q1212 705 1178 668 L880 380 Z" fill="url(#sleeperTone)"/>
  <path d="M470 0 L850 375" stroke="var(--teal-dark)" stroke-width="62" stroke-linecap="round"/>
  <path d="M410 70 L680 335 Q705 355 750 336" fill="none" stroke="var(--white)" stroke-width="4"/>
  <path d="M400 920 L720 1240" stroke="var(--teal-dark)" stroke-width="62" stroke-linecap="round"/>
  <path role="img" aria-label="Photo of a smiling man stretching after waking up rested" d="M55 1060 L262 882 Q292 858 322 882 L610 1172 L55 1172 Z" fill="url(#wakerTone)"/>
  <path d="M55 985 L158 910 Q182 898 204 918" fill="none" stroke="var(--white)" stroke-width="4"/>
  <path d="M1007 1172 L1228 1002 Q1268 972 1310 1002 L1483 1138 L1483 1172 Z" fill="var(--teal)"/>
  <circle role="img" aria-label="Portrait photo of the dentist" cx="767" cy="495" r="76" fill="url(#portraitTone)" stroke="var(--white)" stroke-width="5"/>
  <rect x="709" y="1103" width="136" height="54" rx="3" fill="var(--white)"/>
  <rect x="858" y="1103" width="136" height="54" rx="3" fill="var(--white)"/>
  <path d="M712 412 l3 8 8 3 -8 3 -3 8 -3 -8 -8 -3 8 -3z M840 545 l3 8 8 3 -8 3 -3 8 -3 -8 -8 -3 8 -3z" fill="var(--white)"/>
</svg>

<div class="block heading light" style="left:51px;top:51px;width:190px">Signs you may not know you have Sleep Apnea</div>
<ul class="block tick-list on-teal light" style="left:51px;top:140px;width:205px">
  <li style="margin-bottom:9px"><svg><use href="#tick"/></svg>Gasping, choking or snorting during sleep</li>
  <li style="margin-bottom:9px"><svg><use href="#tick"/></svg>Waking up tired despite the full night sleep</li>
  <li style="margin-bottom:9px"><svg><use href="#tick"/></svg>Waking up with dry mouth / sore throat</li>
  <li style="margin-bottom:9px"><svg><use href="#tick"/></svg>Waking up with a headache</li>
  <li style="margin-bottom:9px"><svg><use href="#tick"/></svg>Feeling sleepy or tired during the day despite a full night's sleep</li>
  <li style="margin-bottom:9px"><svg><use href="#tick"/></svg>Falling asleep in inappropriate situations (movies, church, sitting quietly)</li>
  <li style="margin-bottom:9px"><svg><use href="#tick"/></svg>Problems with memory and concentration</li>
  <li style="margin-bottom:9px"><svg><use href="#tick"/></svg>Being ill-tempered or irritable</li>
  <li style="margin-bottom:9px"><svg><use href="#tick"/></svg>Depression</li>
  <li style="margin-bottom:9px"><svg><use href="#tick"/></svg>Nightmares</li>
  <li style="margin-bottom:9px"><svg><use href="#tick"/></svg>Irregular heartbeat</li>
  <li><svg><use href="#tick"/></svg>Nighttime teeth grinding/ tapping</li>
</ul>

<div class="block doctor-name" style="left:266px;top:300px;width:234px">Dr. Lena Hoshino, DMD</div>
<div class="block doctor-bio" style="left:279px;top:326px;width:208px">
  <p>Dr. Lena Hoshino graduated from Cascadia Health University School of Dentistry and began practicing in 1999. Throughout her dental career, she has attended countless hours of continuing education to advance her knowledge and skills in dentistry to better serve her patients. She has been always fascinated by the correlation between oral health and systemic disease.</p>
  <p>Eventually, she realized that a dentist could directly contribute to patients' overall health. By recognizing certain appearances in the mouth, she could screen for sleep apnea which is a life-threatening condition. She became passionate about treating sleep apnea by providing each patient with a custom-fit oral appliance.</p>
</div>

<div class="block brand" style="left:540px;top:92px;width:160px">
  <div style="font-size:14px;letter-spacing:.6px">Starlit Sleep</div>
  <div style="font-size:9px;margin-top:1px">Dentistry</div>
</div>
<div class="block cover-title" style="left:505px;top:366px;width:236px">Do You<br><span class="accent">Have Sleep</span><br>Apnea?</div>
<div class="block contact" style="left:540px;top:518px;width:160px;font-size:6.5px;font-weight:500">Starlit Sleep Dentistry</div>
<div class="block contact" style="left:505px;top:542px;width:230px;font-size:11px">
  <svg viewBox="0 0 16 16"><path fill="currentColor" d="M3.6 1.2l2.3 2.6-1.3 2a9 9 0 0 0 5.6 5.6l2-1.3 2.6 2.3-1.4 2.3C7.5 14.6 1.4 8.5 1.3 2.6z"/></svg>(555)010-2468
</div>
<div class="block contact" style="left:505px;top:563px;width:240px;font-size:8.5px">
  <svg viewBox="0 0 16 16"><circle cx="8" cy="8" r="7" fill="currentColor"/><path d="M1.5 8h13M8 1c2.5 2.5 2.5 11.5 0 14M8 1c-2.5 2.5-2.5 11.5 0 14" stroke="var(--teal)" stroke-width="1.2" fill="none"/></svg>www.StarlitSleepDentistry.com
</div>

<!-- ============ INSIDE SHEET ============ -->
<svg class="sheet-art sheet-inside" viewBox="55 1235 1428 1102" preserveAspectRatio="none">
  <defs>
    <linearGradient id="restlessTone" x1="0" y1="0" x2="1" y2="1">
      <stop offset="0" stop-color="#1d2c44"/><stop offset=".5" stop-color="#4d5f80"/><stop offset="1" stop-color="#8fa0bc"/>
    </linearGradient>
    <linearGradient id="laughTone" x1="0" y1="0" x2="1" y2="1">
      <stop offset="0" stop-color="#d7c3b0"/><stop offset=".5" stop-color="#f1ece6"/><stop offset="1" stop-color="#e3ddd7"/>
    </linearGradient>
  </defs>
  <rect x="55" y="1235" width="476" height="1102" fill="var(--teal)"/>
  <rect x="530" y="1235" width="477" height="1102" fill="var(--cream)"/>
  <rect x="1007" y="1235" width="476" height="1102" fill="var(--rust)"/>
  <path d="M760 1170 L420 1480" stroke="var(--teal-dark)" stroke-width="62" stroke-linecap="round"/>
  <path role="img" aria-label="Photo of a tired person lying awake in bed at night" d="M55 1235 L620 1235 L330 1522 Q292 1558 254 1522 L55 1330 Z" fill="url(#restlessTone)"/>
  <path d="M55 1428 L158 1492 Q182 1508 206 1488" fill="none" stroke="var(--white)" stroke-width="4"/>
  <rect role="img" aria-label="Illustration of a human body silhouette marking areas affected by untreated sleep apnea" x="770" y="1570" width="200" height="645" rx="40" fill="#e9dbd1"/>
  <path d="M1140 2100 L820 2400" stroke="var(--teal-dark)" stroke-width="62" stroke-linecap="round"/>
  <path role="img" aria-label="Photo of a woman laughing happily in bed after restful sleep" d="M1030 2337 L1228 2060 Q1262 2018 1296 2060 L1483 2265 L1483 2337 Z" fill="url(#laughTone)"/>
  <path d="M1345 2088 Q1380 2060 1412 2092 L1483 2160" fill="none" stroke="var(--white)" stroke-width="4"/>
</svg>

<div class="block heading light" style="left:51px;top:793px;width:215px">What are my options for treating Sleep Apnea?</div>
<div class="block body-copy light" style="left:51px;top:888px;width:200px">There are several options, and it could be alone or combination of the following treatment modalities:</div>
<ul class="block tick-list on-teal light" style="left:51px;top:938px;width:205px">
  <li style="margin-bottom:8px"><svg><use href="#tick"/></svg>CPAP (Continuous Positive Airway Pressure) machine</li>
  <li style="margin-bottom:9px"><svg><use href="#tick"/></svg>Surgery (invasive procedure)</li>
  <li style="margin-bottom:9px"><svg><use href="#tick"/></svg>Oral Appliance</li>
  <li style="margin-bottom:9px"><svg><use href="#tick"/></svg>Teeth Alignment<br>(clear aligners such as Veridonta and Tessaline)</li>
  <li style="margin-bottom:9px"><svg><use href="#tick"/></svg>Laser Treatment</li>
  <li><svg><use href="#tick"/></svg>Myofunctional Therapy</li>
</ul>
<div class="block body-copy light" style="left:51px;top:1097px;width:205px">Oral Appliance, Teeth Alignment, Laser Treatment, and Myofunctional Therapy can be done in a dental office</div>

<div class="block consequence-title" style="left:280px;top:674px;width:205px">Consequences Of Untreated Sleep Apnea</div>
<div class="block conditions" style="left:278px;top:771px;width:110px">
  <div class="group">
    Stroke
    <div class="two-line">Dementia And<br>Alzheimer</div>
    Insomnia<br>Adhd
  </div>
  <div class="group">Heart Disease<br>Heart Failure<br>Coronary Artery Disease<br>High Blood Pressure</div>
  <div class="group">Acid Reflux (Gerd)</div>
  <div class="group tight">octuria<br>Reduced Libido<br>Erectile Dysfunction<br>High Risk Of Divorce
    <div class="two-line">Seperate Sleeping<br>Arrangement With A<br>Partner Rtner</div>
  </div>
  <div style="margin-top:11px">Increased Risk Of Cancer<br>Low Immune System<br>Fibromyalgia<br>Restless Leg Syndrome</div>
</div>

<div class="block heading light" style="left:518px;top:629px;width:215px">How do I find out if I have Sleep Apnea?</div>
<div class="block body-copy light" style="left:518px;top:688px;width:200px">Many signs of sleep apnea can be recognized during your dental visit. Dr. Lena and her dental team can help you initiate the sleep study to determine if you have sleep apnea or not.</div>
<div class="block heading light" style="left:518px;top:752px;width:220px">Benefits of Oral Appliances over CPAP</div>
<ul class="block tick-list on-rust light" style="left:518px;top:814px;width:210px">
  <li style="margin-bottom:9px"><svg><use href="#tick"/></svg>More comfortable to wear than CPAP</li>
  <li style="margin-bottom:9px"><svg><use href="#tick"/></svg>Easier to clean</li>
  <li style="margin-bottom:9px"><svg><use href="#tick"/></svg>Easier to travel as it is very compact</li>
  <li style="margin-bottom:9px"><svg><use href="#tick"/></svg>Quiet as there is no machine next to you</li>
  <li style="margin-bottom:9px"><svg><use href="#tick"/></svg>No dry mouth, throat or nose</li>
  <li style="margin-bottom:9px"><svg><use href="#tick"/></svg>No bloating or gas from the air pressure</li>
  <li style="margin-bottom:8px"><svg><use href="#tick"/></svg>No monthly maintenance and costs to change hoses and face mask</li>
  <li><svg><use href="#tick"/></svg>Looks much sexier than wearing CPAP (No one wants to look like a Commander Vexor in bed)</li>
</ul>

</body>
</html>
```